Brightway Haul & Repair Services, are a company that offers a 'one stop shop' pre-move clean up a

I have already selected a logo which I would like on the front of the business cards along with phone numbers, web address and email which are:
0419574302
www.brightwayhaul.com.au
brightwayhaulrepair@mailbox.example

On the back of the card I would like to list some of the types of service we offer (clean - move - repairs/maintenance) which are:
CLEAN - windows, gutters, solar panels, driveways/paths, carpets.
MOVE - Small/medium size house/office moves, large item pick-up & delivery, yard clean-up and removal.
General maintenance and repairs.

I would like the blue logo on a gray background.

Thanks

```html
<!DOCTYPE html>
<html lang="en">
<head>
<meta charset="utf-8">
<title>Brightway Haul &amp; Repair Services — Business Card</title>
<link rel="stylesheet" href="https://fonts.googleapis.com/css2?family=Open+Sans:wght@400;600;800&display=swap">
<style>
  :root {
    --page: #ffffff;
    --grey-light: #d6d6d6;
    --grey-mid: #a9a9a9;
    --grey-dark: #8a8a8a;
    --brand-blue: #1f62ae;
    --card-blue: #1e63b1;
    --ink: #1b1b1b;
    --white: #ffffff;
    --divider: rgba(255, 255, 255, 0.55);
  }
  * { margin: 0; padding: 0; box-sizing: border-box; }
  html, body {
    width: 1200px;
    height: 1001px;
    overflow: hidden;
    background: var(--page);
    font-family: "Open Sans", Arial, sans-serif;
  }
  .canvas {
    position: relative;
    width: 1200px;
    height: 1001px;
  }
  .card {
    position: absolute;
    overflow: hidden;
  }

  /* Front */
  .card-front {
    left: 27px;
    top: 22px;
    width: 782px;
    height: 483px;
    background: radial-gradient(ellipse at 40% 38%, var(--grey-light) 0%, var(--grey-mid) 55%, var(--grey-dark) 100%);
  }
  .front-name {
    position: absolute;
    left: 0;
    right: 0;
    top: 178px;
    text-align: center;
    color: var(--brand-blue);
    font-weight: 800;
    font-size: 46px;
    line-height: 1.1;
    letter-spacing: 0.5px;
  }
  .front-contact {
    position: absolute;
    left: 0;
    right: 0;
    top: 312px;
    text-align: center;
    font-size: 11px;
    color: var(--ink);
    white-space: nowrap;
  }
  .front-contact .label {
    color: var(--brand-blue);
    font-weight: 600;
  }
  .front-contact .item { margin-right: 6px; }

  /* Back */
  .card-back {
    left: 398px;
    top: 514px;
    width: 777px;
    height: 474px;
    background: var(--card-blue);
    color: var(--white);
  }
  .back-name {
    position: absolute;
    left: 20px;
    width: 340px;
    top: 200px;
    text-align: center;
    font-weight: 800;
    font-size: 28px;
    line-height: 1.15;
  }
  .back-divider {
    position: absolute;
    left: 383px;
    top: 72px;
    width: 1px;
    height: 336px;
    background: var(--divider);
  }
  .services {
    position: absolute;
    left: 384px;
    right: 0;
    top: 90px;
    text-align: center;
    font-size: 16.5px;
    line-height: 1;
  }
  .service-heading {
    font-size: 19px;
    font-weight: 600;
    letter-spacing: 0.5px;
    margin-bottom: 22px;
  }
  .service-heading.move { margin-top: 34px; margin-bottom: 20px; }
  .service-line { margin-bottom: 16px; }
  .service-line span { margin: 0 6px; }
</style>
</head>
<body>
<div class="canvas">

  <section class="card card-front" aria-label="Business card front">
    <h1 class="front-name">Brightway Haul<br>&amp; Repair Services</h1>
    <p class="front-contact">
      <span class="item"><span class="label">Ph.</span> 0419574302</span>
      <span class="item"><span class="label">Web.</span> www.brightwayhaul.com.au</span>
      <span class="item"><span class="label">Mail.</span> brightwayhaulrepair@mailbox.example</span>
    </p>
  </section>

  <section class="card card-back" aria-label="Business card back">
    <h2 class="back-name">Brightway Haul<br>&amp; Repair Services</h2>
    <div class="back-divider"></div>
    <div class="services">
      <h3 class="service-heading">CLEAN</h3>
      <p class="service-line"><span>Windows</span> <span>Gutters</span> <span>Solar Panels</span> <span>Driveways</span></p>
      <p class="service-line"><span>Paths</span> <span>Carpets</span></p>
      <h3 class="service-heading move">MOVE</h3>
      <p class="service-line">Small/Medium Size House &amp; Office Moves</p>
      <p class="service-line">Large Item Pick-Up &amp; Delivery</p>
      <p class="service-line">Yard Clean-Up &amp; Removal.</p>
      <p class="service-line">General Maintenance &amp; Repairs</p>
    </div>
  </section>

</div>
</body>
</html>
```